Dietary supplement, Clean and simple.

Hi,
I’d like to talk about the project,

About us:
We are a dietary supplement (Vitamins, Minerals, amino acids etc.) company.
The goal is to have about 25 products at the end of this year. However, for this goal to be achieved we need a good label design to make our products represent our company values.
I’ll be here every day supporting your questions, we are fully committed to making the highest/best quality/customer experience possible.

About the design and our values:
- Professional (We are in the industry of professionalism and expertise. I would love to show we are competent at this, Id. Like to have the labels looks like we have done our research.)
- Efficient (White spacing, good use of the space available.)
- Simple (Straight forward, in 5 seconds they have to know what the product they have is/how functions. We’re trying to simplify it for the consumer.
- No distractions (the only visually “distracting” factor can be the vector art.)

The guidelines:
The goal is to have a universal design, with one element that changes (Vector art). I’ll attach a file/multiple files I think can show some visuals on what I’m looking for, and what parts of the design I think are good/bad.

Label size: 69x155mm (Front is 77.5mm)

Design whatever you think fits our image. You’re the design expert, all I care about is that it fits our company standards/image.

Use this color/font.
Font: Sans Serif
Main company color is Mind green #237D62 (Use this color for something in the design.)

What I thought would be cool/might looks ugly, who knows:
1. The front of the label: Should have 1 vector art, preferably in the top right corner. (That looks good in multiple colors. The vector can have multiple areas to color, I would prefer 2 main colors in the vector art. The interchangeable colors are used for multiple kinds of products.)
2. Text/product information on the left. The text that will have to be displayed:
- Product name for instance “Magnesium + B6”
- Description for the product for instance “Magnesium with ginger taste”
- Company name or logo. (Add ® behind it. We are soon to be trademark registered.)
3. We need to show the "daily intake" amount on the front and also the amount in the complete bottle. For instance, “Daily intake 1 capsule, 60 capsules”.
• You don’t have to design the backside of the label. After I chose a design, I’d like to chat and give specific information on what areas need to be assigned where. (Too complex because of the law.)
Updates

Hi, Please make the deadline 31 days total. I want designers to have the time to design. And not be rushed to finish it.

I want to extend the deadline because i feel like a slightly more medical look would be interesting. Hope you can come up with something!!

Target Market(s)

Dietary supplement consumers

Industry/Entity Type

Dietary supplements

Font styles to use
Sans Serif

Colors

Designer to choose colors to be used in the design.

Requirements
Must have
• Trademark icon "®" has to be at the top right after the company logo(text of logo)/name.

```html
<!DOCTYPE html>
<html lang="en">
<head>
<meta charset="UTF-8">
<title>Magnesium + B6 Label</title>
<link href="https://fonts.googleapis.com/css2?family=Inter:wght@400;600;700&display=swap" rel="stylesheet">
<style>
  :root {
    --canvas-bg: #f9f3f2;
    --label-dark: #bdbdbd;
    --label-light: #f4f4f4;
    --ink: #0d0d0d;
    --brand-green: #13672b;
    --mind-green: #1e6e55;
    --art-purple: #7a3a78;
    --art-orange: #c9552b;
    --white: #ffffff;
  }
  * { margin: 0; padding: 0; box-sizing: border-box; }
  html, body {
    width: 1200px;
    height: 1200px;
    overflow: hidden;
    background: var(--canvas-bg);
    font-family: "Inter", Arial, sans-serif;
  }
  .label {
    position: absolute;
    left: 120px;
    top: 62px;
    width: 960px;
    height: 1075px;
    overflow: hidden;
    background: linear-gradient(90deg, var(--label-dark) 0%, #cfcfcf 30%, #e2e2e2 60%, var(--label-light) 80%, #dedede 100%);
  }
  .vector-art {
    position: absolute;
    left: 740px;
    top: 0;
    width: 220px;
    height: 790px;
    background: linear-gradient(180deg, var(--art-purple) 0%, #9a4a76 55%, var(--art-orange) 100%);
    opacity: 0.85;
  }
  .brand {
    position: absolute;
    left: 100px;
    top: 180px;
    color: var(--brand-green);
    font-weight: 700;
  }
  .brand-mark {
    width: 46px;
    height: 46px;
    border-radius: 50%;
    background: var(--brand-green);
    margin: 0 0 14px 150px;
  }
  .brand-name {
    font-size: 78px;
    line-height: 1;
    letter-spacing: -1px;
  }
  .brand-reg {
    font-size: 26px;
    vertical-align: top;
    margin-left: 4px;
    letter-spacing: 0;
  }
  .brand-sub {
    font-size: 34px;
    letter-spacing: 20px;
    margin: 14px 0 0 52px;
  }
  .product-name {
    position: absolute;
    left: 100px;
    top: 500px;
    font-size: 72px;
    font-weight: 700;
    color: var(--ink);
    letter-spacing: -0.5px;
  }
  .product-desc {
    position: absolute;
    left: 102px;
    top: 600px;
    font-size: 24px;
    font-weight: 400;
    letter-spacing: 4.5px;
    color: var(--ink);
  }
  .quantity {
    position: absolute;
    left: 106px;
    top: 800px;
    display: flex;
    align-items: baseline;
    color: var(--ink);
  }
  .quantity-number {
    font-size: 80px;
    font-weight: 600;
    line-height: 1;
    letter-spacing: -2px;
  }
  .quantity-unit {
    font-size: 24px;
    letter-spacing: 2px;
    margin-left: 12px;
  }
  .daily-intake {
    position: absolute;
    left: 92px;
    top: 882px;
    height: 42px;
    padding: 0 30px 0 22px;
    border-radius: 21px;
    background: var(--mind-green);
    color: var(--white);
    font-size: 23px;
    font-weight: 700;
    letter-spacing: 1.5px;
    line-height: 42px;
  }
</style>
</head>
<body>
  <main class="label">
    <div class="vector-art" role="img" aria-label="Interchangeable brush-stroke vector artwork in purple and orange"></div>

    <div class="brand">
      <div class="brand-mark"></div>
      <div class="brand-name">VERDANT<span class="brand-reg">®</span></div>
      <div class="brand-sub">CALM</div>
    </div>

    <h1 class="product-name">Magnesium + B6</h1>
    <p class="product-desc">MAGNESIUM WITH GINGER TASTE</p>

    <div class="quantity">
      <span class="quantity-number">60</span>
      <span class="quantity-unit">CAPSULES</span>
    </div>

    <div class="daily-intake">DAILY INTAKE 1 CAPSULE</div>
  </main>
</body>
</html>
```